Concept design for a tea business Labels

Hello, we are looking for concepts for our label/packaging for a tea business that has been in business now for over a year. We are a beachy, organic, "It's your moment. Enjoy it." type tea business. We have an online website (www.corvalbrewhouse.com.au) and sell at local markets around the Tarrowby Cove area.
We are looking to upgrade our label to look more professional, in a fun/beachy/chilled out style. (unlike the traditional tea labels).
We do loose leaf tea and iced tea consentrated syrups. We have a few different packages (please see website under "sizes and packaging" bottom left). We would like to experiement with various different size and shape of labels for different products, so would like a concept design for a label using our logo (see website front page bottom). There are no colour constraints.
We use the Quillan brand labels of the following sizes:
1. Pure Glass Rectangular Product Labels, Q4825, 100/Pack, 96 x 50.8 mm
2. Pure Glass Round Multi-purpose Labels, Q3907D, 240/Pack, 40 mm diameter
3.Pure Glass Square Product Labels, Q4861, 350/Pack, 35 x 35 mm
4. For bottles we use Grained Ivory Curved Labels, Q4839, 90/Pack, 57.2 x 77 mm
If you have any more questions, please don't hesitate to contact me
Updates
Hi All,
I am considering using a box like below for packing and doing a bit of a white/beachy feel to the packaging. Either using the rectangle or round circle labels. (circle labels from quillan 60mm diameter).

Reason: Hi All - Thank you so much for all your designs. While I have seen some really beautiful designs I am excited about, it seems there was a rush at the end with a number of new designs just submitted. I still haven't seen just one design I love for the label, so I would like the opportunity to work with some of the new designers to see if we can modify to suit the concept.
Would anyone like to try a concept label with a silhouette of one of the following wave/beach/teacup? I'm just exploring a different approach as I know it is difficult tying in the beach with tea - please think - chilled out beach hut with tea/iced tea, sunrise over ocean. I like the soft colour palette - beachy feel to it - ie. Pastels - blues, greens, whites, sandy, pinks, purples, greys - sunrises over ocean, maybe a white rustic wood feel - or any other icon from Tarrowby Cove - like the Norfolk Pine's along the beach - maybe in Silhouette.
Just some more ideas.
Thank you again for all your contributions!
Petra

```html
<!DOCTYPE html>
<html lang="en">
<head>
<meta charset="utf-8">
<title>Tarrowby Tea Company – Label Concepts</title>
<link rel="stylesheet" href="https://fonts.googleapis.com/css2?family=Oswald:wght@400;500&family=Roboto:wght@700&display=swap">
<style>
  :root {
    --page: #ffffff;
    --sand: #dccb98;
    --leaf: #a9a878;
    --olive: #4a4d2e;
    --orange: #f47a3c;
    --outline: #5a3a22;
    --ink: #111111;
    --white: #ffffff;
  }
  html, body {
    margin: 0;
    width: 1200px;
    height: 1000px;
    overflow: hidden;
    background: var(--page);
  }
  .sheet { display: block; width: 1200px; height: 1000px; }
  .caption {
    font-family: "Roboto", Arial, sans-serif;
    font-weight: 700;
    fill: var(--ink);
  }
  .label-bg { fill: var(--sand); }
  .band { fill: var(--olive); }
  .company {
    font-family: "Oswald", sans-serif;
    font-weight: 400;
    fill: var(--olive);
    text-anchor: middle;
  }
  .product {
    font-family: "Oswald", sans-serif;
    font-weight: 500;
    fill: var(--orange);
    stroke: var(--outline);
    stroke-width: 1.5px;
    paint-order: stroke;
    text-anchor: middle;
    letter-spacing: 2px;
  }
  .weight {
    font-family: "Oswald", sans-serif;
    font-weight: 400;
    fill: var(--olive);
    text-anchor: middle;
    letter-spacing: 2px;
  }
  .tagline {
    font-family: "Oswald", sans-serif;
    font-weight: 400;
    fill: var(--white);
    text-anchor: middle;
    letter-spacing: 3px;
  }
  .brand-name {
    font-family: "Oswald", sans-serif;
    font-weight: 500;
    fill: var(--orange);
    text-anchor: start;
  }
  .brand-dot { fill: var(--orange); }
</style>
</head>
<body>
<svg class="sheet" viewBox="0 0 1200 1000" xmlns="http://www.w3.org/2000/svg">
  <defs>
    <radialGradient id="foliage" cx="50%" cy="60%" r="55%">
      <stop offset="0%" stop-color="#a3a474" stop-opacity="0.75"/>
      <stop offset="100%" stop-color="#dccb98" stop-opacity="0"/>
    </radialGradient>
    <clipPath id="clip-rect"><rect x="42" y="65" width="724" height="382"/></clipPath>
    <clipPath id="clip-round-small"><circle cx="974" cy="237" r="150"/></clipPath>
    <clipPath id="clip-round-large"><circle cx="381" cy="693" r="227"/></clipPath>
    <clipPath id="clip-square"><rect x="795" y="578" width="264" height="262"/></clipPath>
  </defs>

  <!-- Rectangular label -->
  <text class="caption" x="52" y="50" font-size="27">Q4825, 100/Pack</text>
  <g class="label label--rect" clip-path="url(#clip-rect)">
    <rect class="label-bg" x="42" y="65" width="724" height="382"/>
    <rect x="150" y="65" width="520" height="340" fill="url(#foliage)" role="img" aria-label="Tea plant leaves illustration"/>
    <circle class="brand-dot" cx="318" cy="160" r="10"/>
    <text class="brand-name" x="338" y="172" font-size="34">Tarrowby Tea</text>
    <text class="company" x="405" y="277" font-size="21">TARROWBY TEA COMPANY</text>
    <text class="product" x="405" y="345" font-size="54">Milky Oolong</text>
    <text class="weight" x="400" y="386" font-size="22">200 grms</text>
    <rect class="band" x="42" y="397" width="724" height="50"/>
    <text class="tagline" x="405" y="430" font-size="21">organic tea</text>
  </g>

  <!-- Small round label -->
  <g class="label label--round-small" clip-path="url(#clip-round-small)">
    <circle class="label-bg" cx="974" cy="237" r="150"/>
    <rect x="840" y="87" width="270" height="250" fill="url(#foliage)" role="img" aria-label="Tea plant leaves illustration"/>
    <circle class="brand-dot" cx="910" cy="145" r="6"/>
    <text class="brand-name" x="924" y="153" font-size="22">Tarrowby Tea</text>
    <text class="company" x="973" y="245" font-size="19">TARROWBY TEA COMPANY</text>
    <text class="product" x="968" y="293" font-size="34">Milky Oolong</text>
    <text class="weight" x="970" y="325" font-size="16">100 grms</text>
    <rect class="band" x="820" y="335" width="310" height="60"/>
    <text class="tagline" x="971" y="366" font-size="17">organic tea</text>
  </g>
  <text class="caption" x="970" y="430" font-size="28" text-anchor="middle">Q3907D, 240/Pack</text>

  <!-- Large round label -->
  <g class="label label--round-large" clip-path="url(#clip-round-large)">
    <circle class="label-bg" cx="381" cy="693" r="227"/>
    <rect x="160" y="466" width="440" height="372" fill="url(#foliage)" role="img" aria-label="Tea plant leaves illustration"/>
    <circle class="brand-dot" cx="288" cy="545" r="10"/>
    <text class="brand-name" x="308" y="557" font-size="34">Tarrowby Tea</text>
    <text class="company" x="381" y="676" font-size="24">TARROWBY TEA COMPANY</text>
    <text class="product" x="381" y="751" font-size="54">Milky Oolong</text>
    <text class="weight" x="376" y="808" font-size="22">200 grms</text>
    <rect class="band" x="150" y="837" width="470" height="90"/>
    <text class="tagline" x="381" y="880" font-size="24">organic tea</text>
  </g>
  <text class="caption" x="380" y="956" font-size="28" text-anchor="middle">quillan 60mm diameter</text>

  <!-- Square label -->
  <g class="label label--square" clip-path="url(#clip-square)">
    <rect class="label-bg" x="795" y="578" width="264" height="262"/>
    <rect x="795" y="578" width="264" height="222" fill="url(#foliage)" role="img" aria-label="Tea plant leaves illustration"/>
    <circle class="brand-dot" cx="866" cy="637" r="6"/>
    <text class="brand-name" x="880" y="645" font-size="22">Tarrowby Tea</text>
    <text class="company" x="929" y="711" font-size="19">TARROWBY TEA COMPANY</text>
    <text class="product" x="926" y="755" font-size="32">Milky Oolong</text>
    <text class="weight" x="928" y="785" font-size="16">100 grms</text>
    <rect class="band" x="795" y="800" width="264" height="40"/>
    <text class="tagline" x="927" y="827" font-size="16">organic tea</text>
  </g>
  <text class="caption" x="928" y="898" font-size="28" text-anchor="middle">Q4861, 350/Pack</text>
</svg>
</body>
</html>
```